Clara Whitfield: Adult Models Flyer

We need an attractive flyer design to promote our adult modeling agency and recruit models to our business. We hire beautiful, young women and couples to be on a live adult camshow. We would like to highlight the following features of this job position:

-Pays $100/hour
-Set your own schedule
-Have fun and get paid
-Sign up at cwadultmodels.example

The theme should be similar to the website (hot pink and white). We are putting these flyers around college campuses and nightclubs.
Updates

Just uploaded a couple pics of me and my new model that might work well on the flyer(:

Target Market(s)

Our audience is attractive, young women (college students, baristas, waitresses etc.)

Industry/Entity Type

College

Requirements
Must have
• A picture of Clara Whitfield. Perhaps a long body shot on the side or just her face somewhere. Pictures can be found here: https://chirpnet.example/WhitfieldClara
and here: http://picvue.example/whitfieldclara

A visible and bold area featuring: "$100/hour"

```html
<!DOCTYPE html>
<html lang="en">
<head>
<meta charset="utf-8">
<title>Clara Whitfield – Adult Models Flyer</title>
<link href="https://fonts.googleapis.com/css2?family=Kaushan+Script&display=swap" rel="stylesheet">
<style>
  :root {
    --page-bg: #f3eef0;
    --paper: #ffffff;
    --pink-soft: #f6d9ee;
    --pink-light: #eebfe2;
    --pink-band: rgba(214, 130, 196, 0.88);
    --pink-band-solid: #dc8fcb;
    --pink-hot: #d2359a;
    --pink-deep: #b01c7d;
    --skin: #f2d2bd;
    --cream: #f7ead9;
    --white: #ffffff;
  }
  * { margin: 0; padding: 0; box-sizing: border-box; }
  html, body { width: 1200px; height: 1000px; overflow: hidden; }
  body {
    background: var(--page-bg);
    font-family: "Kaushan Script", cursive;
    position: relative;
  }
  .flyer {
    position: absolute;
    left: 385px;
    top: 17px;
    width: 430px;
    height: 966px;
    background: linear-gradient(180deg, var(--paper) 0%, var(--pink-soft) 30%, var(--pink-light) 100%);
    box-shadow: 0 4px 18px rgba(80, 20, 60, 0.18);
    overflow: hidden;
  }
  .brand {
    position: absolute;
    left: 0;
    right: 0;
    top: 40px;
    display: flex;
    align-items: center;
    justify-content: center;
    gap: 12px;
    z-index: 3;
  }
  .brand-dot {
    width: 26px;
    height: 26px;
    border-radius: 50%;
    background: var(--pink-hot);
  }
  .brand-name {
    font-size: 38px;
    color: var(--pink-hot);
    line-height: 1;
  }
  .hero-photo {
    position: absolute;
    left: 110px;
    right: 0;
    top: 130px;
    height: 660px;
    z-index: 1;
    background:
      radial-gradient(ellipse 32% 16% at 70% 16%, #e9c79a 0%, rgba(233,199,154,0) 100%),
      radial-gradient(ellipse 45% 28% at 60% 48%, var(--cream) 0%, rgba(247,234,217,0) 100%),
      radial-gradient(ellipse 60% 50% at 58% 50%, var(--skin) 0%, rgba(242,210,189,0.6) 55%, rgba(238,191,226,0) 100%);
  }
  .perks {
    position: absolute;
    left: 0;
    top: 175px;
    width: 250px;
    list-style: none;
    z-index: 2;
  }
  .perk {
    background: var(--pink-band);
    color: var(--white);
    font-size: 21px;
    line-height: 1.3;
    padding: 14px 14px 14px 22px;
    margin-bottom: 8px;
    min-height: 88px;
    display: flex;
    flex-direction: column;
    justify-content: center;
  }
  .perk-url { white-space: nowrap; }
  .rate-badge {
    position: absolute;
    left: 14px;
    top: 540px;
    width: 180px;
    height: 160px;
    z-index: 2;
  }
  .rate-badge svg { position: absolute; inset: 0; }
  .rate-text {
    position: absolute;
    inset: 0;
    display: flex;
    flex-direction: column;
    align-items: center;
    justify-content: center;
    color: var(--white);
    line-height: 1;
  }
  .rate-amount { font-size: 46px; }
  .rate-unit { font-size: 26px; margin-top: 2px; }
  .gallery-band {
    position: absolute;
    left: 0;
    right: 0;
    top: 790px;
    height: 130px;
    background: var(--pink-band-solid);
    display: flex;
    align-items: center;
    justify-content: space-between;
    padding: 0 10px;
    z-index: 2;
  }
  .thumb {
    width: 76px;
    height: 100px;
    border: 3px solid var(--white);
  }
  .thumb-1 { background: linear-gradient(135deg, #e9c4a8, #c98e8e); }
  .thumb-2 { background: linear-gradient(135deg, #e6c9a0, #d27ab0); }
  .thumb-3 { background: linear-gradient(180deg, #8fc4e8, #4f9ac8); }
  .thumb-4 { background: linear-gradient(135deg, #6e4b4b, #c9464f); }
  .thumb-5 { background: linear-gradient(135deg, #f1dcc0, #3a3238); }
  .footer-strip {
    position: absolute;
    left: 0;
    right: 0;
    bottom: 0;
    height: 46px;
    background: linear-gradient(180deg, var(--pink-light), var(--pink-band-solid));
  }
</style>
</head>
<body>
  <main class="flyer">
    <header class="brand">
      <span class="brand-dot"></span>
      <span class="brand-name">Clara Whitfield</span>
    </header>

    <div class="hero-photo" role="img" aria-label="Photo of a smiling blonde model in a striped tank top and white shorts"></div>

    <ul class="perks">
      <li class="perk"><span>Sign up at</span><span class="perk-url">cwadultmodels.example</span></li>
      <li class="perk"><span>Set your</span><span>own schedule</span></li>
      <li class="perk"><span>Have fun and</span><span>get paid</span></li>
    </ul>

    <div class="rate-badge">
      <svg viewBox="0 0 180 160" aria-hidden="true">
        <polygon fill="var(--pink-hot)" stroke="var(--white)" stroke-width="3"
          points="168,80 153.8,97.1 157.5,119 136.7,126.7 129,147.5 107.1,143.8 90,158 72.9,143.8 51,147.5 43.3,126.7 22.5,119 26.2,97.1 12,80 26.2,62.9 22.5,41 43.3,33.3 51,12.5 72.9,16.2 90,2 107.1,16.2 129,12.5 136.7,33.3 157.5,41 153.8,62.9"/>
      </svg>
      <div class="rate-text">
        <span class="rate-amount">$100</span>
        <span class="rate-unit">per hour</span>
      </div>
    </div>

    <section class="gallery-band">
      <div class="thumb thumb-1" role="img" aria-label="Photo of two models posing together"></div>
      <div class="thumb thumb-2" role="img" aria-label="Photo of two models in swimwear"></div>
      <div class="thumb thumb-3" role="img" aria-label="Photo of a model by a pool"></div>
      <div class="thumb thumb-4" role="img" aria-label="Photo of a model in a sports jersey on a sofa"></div>
      <div class="thumb thumb-5" role="img" aria-label="Photo of two models in black tops"></div>
    </section>

    <div class="footer-strip"></div>
  </main>
</body>
</html>
```